Private chef located in Vail, CO

I would like my info located at the top of the landing page, perhaps some Vail mountain landscapes that I could swap out from summer to winter photos. I need the menu bar to have a link to a blog, about me, photo gallery, recipes & beer reviews. I would also like to have a shop, but only populated with products from quolex or other online retailers that I can affiliate with.
Target Market(s)
Extremely wealthy, affluent people, concierge, international
Number of Pages Required
5+ page

```html
<!DOCTYPE html>
<html lang="en">
<head>
<meta charset="utf-8">
<title>Daniel Whitford — Private Chef</title>
<link href="https://fonts.googleapis.com/css2?family=Montserrat:wght@700&family=Open+Sans:ital,wght@0,400;0,600;0,700;0,800;1,400&display=swap" rel="stylesheet">
<style>
  :root {
    --orange: #f68d22;
    --orange-deep: #ee7f10;
    --sky-top: #a9c6ea;
    --sky-mid: #c9dcf3;
    --mountain: #6f93c6;
    --white: #ffffff;
    --grey-text: #6b6b6b;
    --footer: #111111;
    --backdrop: #f2f2f2;
  }
  * { box-sizing: border-box; margin: 0; padding: 0; }
  html, body { width: 1200px; height: 1200px; overflow: hidden; }
  body { background: var(--backdrop); font-family: "Open Sans", Arial, sans-serif; }

  .page {
    position: absolute; left: 64px; top: 0;
    width: 1072px; height: 1200px;
    background: var(--white); overflow: hidden;
  }

  .hero-backdrop {
    position: absolute; left: 0; top: 0; width: 1072px; height: 460px;
    background:
      radial-gradient(ellipse 330px 260px at 536px 330px, var(--mountain) 0%, rgba(111,147,198,0.55) 45%, rgba(111,147,198,0) 75%),
      linear-gradient(180deg, var(--sky-top) 0%, var(--sky-mid) 55%, var(--white) 100%);
  }

  .site-nav {
    position: absolute; left: 0; top: 0; width: 1072px; height: 81px;
    background: rgba(220, 233, 250, 0.55);
  }
  .site-nav a {
    position: absolute; top: 33px;
    font-size: 13px; color: var(--white); text-decoration: none; letter-spacing: 0.2px;
  }
  .site-nav a.is-active { color: var(--orange); font-weight: 700; }
  .nav-cart { position: absolute; left: 773px; top: 34px; }
  .call-button {
    position: absolute; left: 829px; top: 26px; width: 92px; height: 26px;
    border-radius: 13px; background: var(--orange); color: var(--white);
    font-size: 10px; font-weight: 700; text-align: center; line-height: 26px;
  }

  .hero-title {
    position: absolute; left: 0; top: 118px; width: 1072px; text-align: center;
    font-family: "Montserrat", Arial, sans-serif; font-weight: 700;
    font-size: 80px; line-height: 76px; color: var(--white);
    text-shadow: 4px 4px 0 var(--orange);
  }

  .portrait {
    position: absolute; left: 460px; top: 315px; width: 152px; height: 152px;
    border-radius: 50%; border: 3px solid var(--orange);
    background: radial-gradient(circle at 40% 45%, #c79b7a 0%, #6b5444 45%, #2b2622 100%);
  }

  .intro-heading {
    position: absolute; left: 0; top: 514px; width: 1072px; text-align: center;
    font-size: 33px; font-weight: 800; color: var(--orange);
  }
  .intro-quote {
    position: absolute; left: 0; top: 583px; width: 1072px; text-align: center;
    font-size: 34px; font-style: italic; line-height: 54px; color: var(--grey-text);
  }
  .read-more {
    position: absolute; left: 470px; top: 732px; width: 131px; height: 36px;
    border-radius: 8px; background: var(--orange); color: var(--white);
    font-size: 13px; font-weight: 700; text-align: center; line-height: 36px;
  }

  .contact-band {
    position: absolute; left: 0; top: 836px; width: 1072px; height: 315px;
    background: var(--orange); color: var(--white);
  }
  .band-heading {
    position: absolute; left: 0; width: 1072px; text-align: center;
    font-size: 33px; font-weight: 800;
  }
  .contact-list {
    position: absolute; left: 0; top: 98px; width: 1072px;
    display: flex; justify-content: center; gap: 26px;
    font-size: 20px; font-weight: 700;
  }
  .contact-item { display: flex; align-items: center; gap: 10px; }
  .message-form {
    position: absolute; left: 218px; top: 264px; display: flex; gap: 16px;
  }
  .message-field {
    width: 147px; height: 25px; border: 2px solid var(--white); border-radius: 13px;
    font-size: 10px; line-height: 21px; padding-left: 14px;
  }
  .send-button {
    width: 147px; height: 25px; margin-left: 1px; border-radius: 13px;
    background: var(--white); color: var(--orange);
    font-size: 13px; font-weight: 700; text-align: center; line-height: 25px;
  }

  .site-footer {
    position: absolute; left: 0; top: 1151px; width: 1072px; height: 49px;
    background: var(--footer); color: var(--white);
    font-size: 10px; text-align: center; line-height: 49px;
  }
</style>
</head>
<body>
<main class="page">
  <div class="hero-backdrop" role="img" aria-label="Photo of a snow-covered mountain peak rising above clouds against a blue sky"></div>

  <nav class="site-nav">
    <a class="is-active" style="left:237px">ABOUT ME</a>
    <a style="left:335px">GALLERY</a>
    <a style="left:420px">RECIPES</a>
    <a style="left:500px">BEER REVIEWS</a>
    <a style="left:620px">BLOG</a>
    <a style="left:684px">CONTACT</a>
    <svg class="nav-cart" width="16" height="14" viewBox="0 0 16 14" aria-label="Shop cart">
      <path d="M0 1h3l2 8h8l2-6H4" fill="none" stroke="#fff" stroke-width="1.8"/>
      <path d="M4.5 3h10.5l-2 6H6z" fill="#fff"/>
      <circle cx="6" cy="12" r="1.5" fill="#fff"/><circle cx="12" cy="12" r="1.5" fill="#fff"/>
    </svg>
    <div class="call-button">CALL US</div>
  </nav>

  <h1 class="hero-title">DANIEL<br>WHITFORD</h1>

  <div class="portrait" role="img" aria-label="Portrait photo of the chef in a cap, smiling in a kitchen"></div>

  <h2 class="intro-heading">Get to know me Better</h2>
  <p class="intro-quote">“ Innovative technique attention to detail,<br>focus on exceeding the guests expectations. ”</p>
  <div class="read-more">READ MORE</div>

  <section class="contact-band">
    <h2 class="band-heading" style="top:14px">Contact</h2>
    <div class="contact-list">
      <span class="contact-item">
        <svg width="24" height="24" viewBox="0 0 24 24" aria-hidden="true"><path d="M6 2l4 4-2 3c1.5 3 4 5.5 7 7l3-2 4 4-3 3C11 20 4 13 3 5z" fill="none" stroke="#fff" stroke-width="1.4" stroke-linejoin="round"/></svg>
        +15550147208
      </span>
      <span class="contact-item">
        <svg width="24" height="24" viewBox="0 0 24 24" aria-hidden="true"><circle cx="12" cy="12" r="10" fill="none" stroke="#fff" stroke-width="1.6"/></svg>
        +15550147208
      </span>
      <span class="contact-item">
        <svg width="28" height="22" viewBox="0 0 28 22" aria-hidden="true"><rect x="1" y="2" width="26" height="18" fill="none" stroke="#fff" stroke-width="1.4"/><path d="M1 2l13 10L27 2M1 20l10-9M27 20l-10-9" fill="none" stroke="#fff" stroke-width="1.4"/></svg>
        hello@danwhitford.com
      </span>
    </div>
    <h2 class="band-heading" style="top:187px">Send Message</h2>
    <div class="message-form">
      <div class="message-field">Name</div>
      <div class="message-field">E-mail</div>
      <div class="message-field">Phone</div>
      <div class="send-button">SEND</div>
    </div>
  </section>

  <footer class="site-footer">Copyrights 2019. All rights reserved</footer>
</main>
</body>
</html>
```